"Tova's" Website Design

Tova's makes earth friendly, healthy, and delicious snacks that are completely gluten free. We are looking for a website that is easy to navigate, energetic, and conveys our purpose "To create healthy, earth-friendly, gluten free snacks that fill bellies and warm hearts."
Our first product is "Tova's Cheese Bursts" are a small, square, cracker pack with an unreasonable amount of cheddar cheese flavor. The flavor literally explodes in your mouth!
We really want our site to pop and show off some personality.
I'm attaching the logo for the company, feel free to go beyond the logo in terms of color.
Here are some sites that we like!
http://www.pollwinkle.example/company
http://www.brenmoor.example/
http://www.qx47.example/
http://www.teddyvales.example/
http://www.dunrise.example/food/products_zest/
http://www.marvelfrost.example/

```html
<!DOCTYPE html>
<html lang="en">
<head>
<meta charset="utf-8">
<title>Tova's – The Crackers</title>
<link href="https://fonts.googleapis.com/css2?family=Arvo:wght@400;700&family=Gochi+Hand&family=Rye&family=Roboto:wght@400;500;700&display=swap" rel="stylesheet">
<style>
:root{
  --navy:#0d2c52;
  --navy-deep:#08203f;
  --orange:#ff6a1f;
  --paper:#f1e3c0;
  --folder:#e2ab3a;
  --folder-dark:#c98f26;
  --ink:#6b4418;
  --wood:#4a2c15;
  --wood-dark:#2b170a;
  --white:#ffffff;
  --black:#111111;
}
*{box-sizing:border-box;margin:0;padding:0}
html,body{width:1200px;height:966px;overflow:hidden}
body{position:relative;background:var(--paper);font-family:"Roboto",Arial,sans-serif;color:var(--ink)}
.site-header{position:absolute;left:0;top:0;width:1200px;height:131px;background:linear-gradient(var(--navy-deep),var(--navy))}
.zigzag{position:absolute;left:0;width:1200px;height:12px;background-size:14px 12px}
.zigzag--header{top:131px;background-image:linear-gradient(135deg,var(--navy) 25%,transparent 25%),linear-gradient(225deg,var(--navy) 25%,transparent 25%)}
.zigzag--footer{top:850px;background-image:linear-gradient(315deg,var(--wood) 25%,transparent 25%),linear-gradient(45deg,var(--wood) 25%,transparent 25%)}
.brand{position:absolute;left:148px;top:14px;font-family:"Arvo",serif;font-weight:700;font-size:60px;color:var(--orange);letter-spacing:1px}
.brand-mark{display:inline-block;width:14px;height:14px;background:var(--orange);margin-left:8px;vertical-align:middle}
.main-nav{position:absolute;left:447px;top:54px;display:flex;gap:17px}
.main-nav a{font-family:"Arvo",serif;font-weight:700;font-size:14px;color:var(--white);text-decoration:none;white-space:nowrap}
.search{position:absolute;left:869px;top:54px;display:flex;gap:4px}
.search-field{width:156px;height:23px;border:1px solid #9fb1c7;background:var(--white);font:12px "Roboto",sans-serif;padding:4px 5px;color:#666}
.search-button{width:31px;height:25px;border-radius:3px;background:#2a5b93;display:flex;align-items:center;justify-content:center}
.folder{position:absolute;left:0;top:0}
.characters{position:absolute;left:206px;top:218px;width:292px;height:130px;background:linear-gradient(90deg,#d6a86a,#c99553);border-radius:12px;opacity:.85}
.bubble{position:absolute;left:414px;top:153px;width:158px;height:49px;background:var(--orange);border-radius:10px;color:var(--white);font-family:"Arvo",serif;font-weight:700;font-size:12px;display:flex;align-items:center;justify-content:center;white-space:nowrap}
.bubble::after{content:"";position:absolute;left:24px;bottom:-9px;border:6px solid transparent;border-top:9px solid var(--orange);border-bottom:0}
.section-title{position:absolute;left:508px;top:258px;font-family:"Gochi Hand",cursive;font-size:42px;color:var(--ink);font-weight:400;letter-spacing:1px}
.feature{position:absolute;font-size:11.5px;line-height:1.45;color:var(--ink);white-space:nowrap}
.feature h3{font-size:14.5px;font-weight:500;margin-bottom:1px}
.sign{position:absolute;left:788px;top:158px;width:244px;height:80px;background:linear-gradient(#6a4220,var(--wood));transform:rotate(4deg);color:#f3e6cc;text-align:center;box-shadow:2px 4px 6px rgba(0,0,0,.3)}
.sign-title{font-family:"Rye",serif;font-size:34px;line-height:1;padding-top:10px}
.sign-note{font-family:"Arvo",serif;font-weight:700;font-size:10px;margin-top:4px;white-space:nowrap}
.nutrition{position:absolute;left:882px;top:542px;width:182px;height:272px;overflow:hidden;background:var(--white);border:2px solid #222;padding:6px 8px;transform:rotate(5deg);color:var(--black);font-family:"Roboto",sans-serif;box-shadow:2px 3px 6px rgba(0,0,0,.25)}
.nutrition h4{font-family:"Arvo",serif;font-weight:700;font-size:18px;line-height:1.05;white-space:nowrap}
.nutrition .serving{font-size:10px;line-height:1.2;white-space:nowrap}
.nutrition .rule{height:6px;background:var(--black);margin:3px 0 2px}
.nutrition table{width:100%;border-collapse:collapse;font-size:10px}
.nutrition td{border-bottom:1px solid var(--black);padding:1.5px 0;white-space:nowrap;line-height:1.2}
.nutrition td:last-child{text-align:right;font-weight:700}
.nutrition .thick td{border-bottom:4px solid var(--black)}
.nutrition .fine{font-size:7px;line-height:1.25;margin-top:4px}
.nutrition .ingredients{font-size:8.5px;line-height:1.25;margin-top:5px}
.product-box{position:absolute;left:672px;top:676px;width:208px;height:156px;background:linear-gradient(135deg,#c9c032,var(--orange) 45%,#e8541a);transform:skewY(-12deg);border-radius:4px}
.site-footer{position:absolute;left:0;top:862px;width:1200px;height:104px;background:repeating-linear-gradient(90deg,var(--wood) 0 380px,var(--wood-dark) 380px 383px),var(--wood)}
.legal{position:absolute;left:139px;top:48px;display:flex;gap:28px;font-size:12px;color:var(--white)}
.legal strong{font-weight:500}
.social{position:absolute;left:921px;top:38px;display:flex;gap:12px}
.social a{display:block;width:36px;height:36px;border-radius:4px;background:#3a6fa8}
</style>
</head>
<body>
<header class="site-header">
  <div class="brand">Tova's<span class="brand-mark"></span></div>
  <nav class="main-nav">
    <a href="#">About Tova</a><a href="#">Tova's Mission</a><a href="#">Our Products</a><a href="#">Contact Us</a>
  </nav>
  <form class="search">
    <input class="search-field" type="text" value="Search Here" aria-label="Search">
    <span class="search-button"><svg width="18" height="18" viewBox="0 0 18 18"><circle cx="7" cy="7" r="5" fill="none" stroke="#ff7a2a" stroke-width="2.5"/><line x1="11" y1="11" x2="16" y2="16" stroke="#ff7a2a" stroke-width="3"/></svg></span>
  </form>
</header>
<div class="zigzag zigzag--header"></div>

<main>
  <svg class="folder" width="1200" height="966">
    <polygon points="201,242 960,228 976,666 221,687" fill="var(--folder)"/>
    <polygon points="830,226 960,228 962,290 902,326" fill="var(--folder-dark)"/>
    <line x1="813" y1="138" x2="818" y2="160" stroke="#888" stroke-width="2"/>
    <line x1="993" y1="130" x2="998" y2="172" stroke="#888" stroke-width="2"/>
    <g role="img" aria-label="Stack of square cheddar crackers">
      <defs>
        <radialGradient id="crackerTone" cx="40%" cy="40%" r="65%">
          <stop offset="0" stop-color="#ebc48a"/><stop offset=".6" stop-color="#d9a867"/><stop offset="1" stop-color="#b9834a"/>
        </radialGradient>
      </defs>
      <polygon points="222,468 440,400 650,430 762,508 720,540 480,592 400,585 300,535 230,498" fill="url(#crackerTone)"/>
    </g>
    <g fill="none" stroke="var(--ink)" stroke-width="1.5">
      <polyline points="485,417 485,378 532,378"/>
      <polyline points="640,443 747,443 747,411 782,411"/>
      <polyline points="752,505 825,505"/>
      <polyline points="634,545 634,579 735,579"/>
    </g>
  </svg>

  <div class="characters" role="img" aria-label="Two cheerful cracker mascots"></div>
  <div class="bubble">Why are we so good?</div>
  <h2 class="section-title">The Crackers</h2>

  <div class="feature" style="left:543px;top:362px"><h3>Seasoning</h3>Coated in Cheddar Cheese Seasoning.<br>Warning! Explosive flavour!</div>
  <div class="feature" style="left:791px;top:402px"><h3>Crunch</h3>Crunchy tiny gluten free crackers</div>
  <div class="feature" style="left:831px;top:491px"><h3>Bite Size</h3>Perfect size snacks!</div>
  <div class="feature" style="left:745px;top:568px"><h3>Healthy</h3>Made with no artificial<br>ingredients!</div>

  <div class="sign">
    <div class="sign-title">Try It Now!</div>
    <div class="sign-note">Contact us to find your nearest stockist</div>
  </div>

  <div class="nutrition">
    <h4>Nutrition Facts</h4>
    <p class="serving">Serving Size 1 packet (1g)<br>Servings Per Container 50</p>
    <div class="rule"></div>
    <table>
      <tr><td><b>Amount Per Serving</b></td><td></td></tr>
      <tr class="thick"><td><b>Calories</b> 0</td><td></td></tr>
      <tr><td></td><td>% Daily Value*</td></tr>
      <tr><td><b>Total Fat</b> 0g</td><td>0%</td></tr>
      <tr><td><b>Sodium</b> 0mg</td><td>0%</td></tr>
      <tr><td><b>Total Carb</b> less than 1g</td><td>0%</td></tr>
      <tr class="thick"><td><b>Protein</b> 0g</td><td></td></tr>
    </table>
    <p class="fine">Not a significant source of calories from fat, saturated fat, trans fat, cholesterol, dietary fiber, sugars, vitamin A, vitamin C, calcium and iron.<br>* Percent Daily Values are based on a 2,000 calorie diet.</p>
    <p class="ingredients"><b>INGREDIENTS:</b> Dextrose with Maltodextrin, Sucralose.</p>
  </div>

  <div class="product-box" role="img" aria-label="Tova's Cheese Bursts product box"></div>
</main>

<div class="zigzag zigzag--footer"></div>
<footer class="site-footer">
  <div class="legal"><strong>© 2012 Copyright Tova's Food</strong><span>Privacy Policy</span><span>Terms &amp; Conditions</span></div>
  <div class="social">
    <a href="#" aria-label="Social network one"></a>
    <a href="#" aria-label="Social network two" style="background:#4aa3d8"></a>
    <a href="#" aria-label="Video channel" style="background:#d9d4cc"></a>
  </div>
</footer>
</body>
</html>
```